KVO-Business Card Design

I need a modern, professional business card design that includes my logo as the main feature, maybe the entire background with the contact info overlaying or even contact info on the back and the logo full frontal

Neat and organized placement of contact information

Would like to see options in black and white

Target Market(s)

real estate Developers, Construction managers, business and home owners

Industry/Entity Type

Construction

Contact Information for Business Card

KVO Construction
Danny Ferrante
General Contractor

Office: 1-888-902-7315 Ext #1
Cell: 215-730-4162
Fax: 1-888-902-7315

Font styles to use
Serif

Requirements
Must have
• title
• office #
• cell #
• Email
• website
Nice to have
• fax

```html
<!DOCTYPE html>
<html lang="en">
<head>
<meta charset="UTF-8">
<title>KVO-Business Card Design</title>
<link href="https://fonts.googleapis.com/css2?family=Tinos:wght@400;700&display=swap" rel="stylesheet">
<style>
  :root {
    --page-bg: #f1f1f1;
    --card-black: #050505;
    --card-white: #f4f4f2;
    --ink: #111111;
    --ink-light: #ffffff;
    --brand-green: #4fa33f;
    --brand-green-soft: #8fc79a;
    --shadow: rgba(0, 0, 0, 0.18);
  }
  * { box-sizing: border-box; margin: 0; padding: 0; }
  html, body {
    width: 1200px;
    height: 900px;
    overflow: hidden;
    background: var(--page-bg);
    font-family: "Tinos", "Times New Roman", serif;
  }
  .sheet {
    width: 1200px;
    height: 900px;
    display: flex;
    align-items: center;
    justify-content: center;
    gap: 60px;
  }
  .card {
    position: relative;
    width: 520px;
    height: 297px;
    box-shadow: 0 10px 28px var(--shadow);
  }

  /* Front: black with brand name */
  .card--front { background: var(--card-black); }
  .brand {
    position: absolute;
    display: flex;
    align-items: center;
    gap: 10px;
    color: var(--brand-green);
    font-weight: 700;
  }
  .card--front .brand {
    left: 50%;
    top: 42%;
    transform: translate(-50%, -50%);
    font-size: 30px;
  }
  .brand__mark {
    width: 18px;
    height: 18px;
    background: var(--brand-green);
  }
  .front-contact {
    position: absolute;
    left: 0;
    right: 0;
    bottom: 34px;
    text-align: center;
    color: var(--ink-light);
    font-size: 15px;
  }

  /* Back: white with contact details */
  .card--back { background: var(--card-white); color: var(--ink); }
  .identity {
    position: absolute;
    left: 44px;
    top: 30px;
    line-height: 1.15;
  }
  .identity__name { font-size: 22px; font-weight: 700; }
  .identity__title, .identity__company { font-size: 15px; }
  .details {
    position: absolute;
    left: 30px;
    top: 108px;
    display: grid;
    grid-template-columns: 88px auto;
    column-gap: 6px;
    font-size: 14px;
    line-height: 1.2;
  }
  .card--back .brand {
    right: 34px;
    bottom: 34px;
    color: var(--brand-green-soft);
    font-size: 34px;
  }
  .card--back .brand__mark { background: var(--brand-green-soft); width: 22px; height: 22px; }
</style>
</head>
<body>
  <main class="sheet">
    <section class="card card--front" aria-label="Card front">
      <div class="brand"><span class="brand__mark"></span><span class="brand__name">KVO Construction</span></div>
      <p class="front-contact">email : kvohomes@example.com / website :</p>
    </section>

    <section class="card card--back" aria-label="Card back">
      <div class="identity">
        <p class="identity__name">Danny Ferrante</p>
        <p class="identity__title">General Contractor</p>
        <p class="identity__company">KVO Construction</p>
      </div>
      <div class="details">
        <span>Office</span><span>: 1-888-902-7315</span>
        <span>Cell</span><span>: 215-730-4162</span>
        <span>Fax</span><span>: 1-888-902-7315</span>
        <span>Email</span><span>: kvohomes@example.com</span>
        <span>Website</span><span>:</span>
      </div>
      <div class="brand"><span class="brand__mark"></span><span class="brand__name">KVO Construction</span></div>
    </section>
  </main>
</body>
</html>
```